new marketing company logo and business card

design logo and biz card for marketing start up.

My company name needs a brand logo designed: Copper Lantern Marketing Co.
Tagline: Sales - Marketing - Brand Building

Sister Bay is the name of my favorite place, in Wisconsin, but the business is NOT BASED there. It should evoke warmth, friendliness, professionalism, and marketing services from a seasoned marketer.

Target Market(s)

I am selling my services to small business that need help.

Industry/Entity Type

Marketing

Contact Information for Business Card

Copper Lantern Marketing Co. (logo)
Sales - Marketing - Brand Building (tagline)

Dana M. Whitcombe
DanaMWhitcombe@fernlymail.com
555-384-0192 mobile

Font styles to use
Serif
Sans Serif

Colors
f78f20
f37122
f68d4d
00a990
85cae6
33b8a4
faa54b

Requirements
Must have
• a logo
• a business card
Nice to have
• I'd love to see a small subtle reference to Sister Bay built in. Sister bay is named that because there are two islands called ‘sister islands’ that flank the bay. If you google this you will see.
• I like warm, earthy colors. But, I am a fun, approachable, real person. Not stand-offish. Should be warm and appealing yet professional.
Should not have
• nothing cartoon-ish. no child-like fonts. this is a professional business.

```html
<!DOCTYPE html>
<html lang="en">
<head>
<meta charset="UTF-8">
<title>Copper Lantern Marketing Co. — Business Card</title>
<link rel="stylesheet" href="https://fonts.googleapis.com/css2?family=Fredoka:wght@500;600&family=Lato:wght@400;700&display=swap">
<style>
  :root {
    --teal: #33b8a4;
    --teal-deep: #00a990;
    --orange: #f37122;
    --orange-soft: #f78f20;
    --paper: #f0f0f0;
    --ink: #3f3f3f;
    --muted: #8a8a8a;
    --rule: #c9c9c9;
    --stage: #3a3a3a;
    --white: #ffffff;
  }
  * { box-sizing: border-box; margin: 0; padding: 0; }
  html, body { width: 1200px; height: 896px; overflow: hidden; }
  body {
    background: var(--stage);
    font-family: "Lato", Arial, sans-serif;
    position: relative;
  }
  .card {
    position: absolute;
    left: 250px;
    width: 700px;
    height: 400px;
    border-radius: 4px;
    overflow: hidden;
    box-shadow: 0 10px 28px rgba(0,0,0,0.35);
  }
  /* Front */
  .card-front { top: 32px; background: var(--paper); }
  .brand {
    position: absolute;
    left: 150px;
    top: 78px;
    display: flex;
    align-items: center;
  }
  .brand-dot {
    width: 54px; height: 54px;
    border-radius: 50%;
    background: var(--orange);
  }
  .brand-divider {
    width: 1px; height: 86px;
    background: var(--rule);
    margin: 0 22px;
  }
  .brand-name {
    font-family: "Fredoka", "Trebuchet MS", sans-serif;
    font-weight: 600;
    color: var(--teal);
    line-height: 1;
  }
  .brand-name .line-main { display: block; font-size: 40px; letter-spacing: 1px; }
  .brand-name .line-sub { display: block; font-size: 21px; letter-spacing: 1.5px; margin-top: 4px; }
  .brand-tagline {
    display: block;
    margin-top: 8px;
    font-size: 10px;
    letter-spacing: 2px;
    color: var(--muted);
    text-transform: uppercase;
  }
  .contact {
    position: absolute;
    left: 170px;
    top: 222px;
    width: 330px;
  }
  .person-name {
    font-family: "Fredoka", "Trebuchet MS", sans-serif;
    font-weight: 600;
    font-size: 26px;
    letter-spacing: 0.5px;
    text-transform: uppercase;
    padding-bottom: 10px;
    border-bottom: 1px solid var(--rule);
  }
  .person-first { color: var(--teal); }
  .person-last { color: var(--orange); }
  .contact-line {
    font-size: 17px;
    color: var(--ink);
    margin-top: 10px;
  }
  .label-mobile { color: var(--orange); font-weight: 700; }
  .label-email { color: var(--teal); font-weight: 700; }
  .edge-band {
    position: absolute;
    left: 0; right: 0; bottom: 0;
    height: 16px;
    display: flex;
  }
  .edge-band .band-teal { width: 34%; background: var(--teal); }
  .edge-band .band-orange { flex: 1; background: var(--orange); }

  /* Back */
  .card-back {
    top: 464px;
    background: linear-gradient(35deg, var(--teal) 0%, #8a9a68 48%, var(--orange) 100%);
  }
  .back-content {
    position: absolute;
    left: 90px;
    top: 110px;
    color: var(--white);
    font-family: "Fredoka", "Trebuchet MS", sans-serif;
    font-weight: 600;
    line-height: 1;
  }
  .back-name-main { display: block; font-size: 58px; letter-spacing: 2px; }
  .back-name-sub { display: block; font-size: 32px; letter-spacing: 2px; margin-top: 8px; }
  .back-tagline {
    display: block;
    margin-top: 34px;
    font-family: "Lato", Arial, sans-serif;
    font-weight: 400;
    font-size: 18px;
    letter-spacing: 1.5px;
    text-transform: uppercase;
  }
</style>
</head>
<body>
  <section class="card card-front">
    <div class="brand">
      <span class="brand-dot"></span>
      <span class="brand-divider"></span>
      <div>
        <div class="brand-name">
          <span class="line-main">COPPER LANTERN</span>
          <span class="line-sub">MARKETING CO.</span>
        </div>
        <span class="brand-tagline">Sales | Marketing | Brand Building</span>
      </div>
    </div>
    <div class="contact">
      <p class="person-name"><span class="person-first">Dana</span> <span class="person-last">M. Whitcombe</span></p>
      <p class="contact-line"><span class="label-mobile">M:</span> 555-384-0192</p>
      <p class="contact-line"><span class="label-email">E:</span> DanaMWhitcombe@fernlymail.com</p>
    </div>
    <div class="edge-band"><span class="band-teal"></span><span class="band-orange"></span></div>
  </section>

  <section class="card card-back" role="img" aria-label="Soft teal-to-orange gradient background behind the company name">
    <div class="back-content">
      <span class="back-name-main">COPPER LANTERN</span>
      <span class="back-name-sub">MARKETING CO.</span>
      <span class="back-tagline">Sales - Marketing - Brand Building</span>
    </div>
  </section>
</body>
</html>
```